Referral Club PostCard/ Index Card

I need to create an Index card for a Contractor Referral Club. I already did my own door hanger which I can show you. Cost is a factor because I'm just starting my company. You guys have already created my 2 logos when I did a previous logo project so I want to use those logos and colors to create a scheme double sided postcard for my referral club attached to our some examples of other ones I've seen. So, you can 1 of 3 different design/color schemes as a basis:
1) The Black background with Blue Shield
2). The Light Blue background with the white wave (Really like this and the black one)
3). My White background blue/black business card design.
So, 3 different design/color schemes to attack?

You can also look at my website for ideas

http://www.TheLanternPointGuide.example
Updates

I have a picture of the things I want to say on BOTH sides on the Index card/[Post card. Basically, there are two versions that can be created, one with the black background/blue logo motif or one with the white/blue background logo. I bought BOTH designs in my logo contest. Actually 1 is the front of the cards and the other is the back of my card. I'm looking for creativity to get these contractors to join this referral club so I can get more leads.

I have some new logos,, icons and pdfs to submit for consideration

Target Market(s)

Drawing Other Contractors into my Professional Referral Exchange Club

Industry/Entity Type

Public Insurance Adjusting

Font styles to use
Serif
Sans Serif
Other font styles liked:
• Love Zurich font but very few people have it..It is eye drawing!!

Colors
0054AA
0677BA
7BADD7
CADEEF
E8F1F8
0094D4
00A9DD
6FCCEA
C7EBF8
E9F6FB
EE7325
F08F49
F5BC92
FAE3D3
FDF4ED

Requirements
Must have
• My Blue or Black/White color scheme to stay consistent to what Ive already had done
Nice to have
• Something that jumps off to entice them to join that I haven't thought of.

```html
<!DOCTYPE html>
<html lang="en">
<head>
<meta charset="utf-8">
<title>The Lantern Point Guide – Lead Program Card</title>
<link href="https://fonts.googleapis.com/css2?family=Roboto:wght@400;500;700;900&family=Tinos&display=swap" rel="stylesheet">
<style>
  :root {
    --blue-top: #0099dc;
    --blue-mid: #0a78c2;
    --blue-bottom: #3d5aa6;
    --sky-light: #e9f4fb;
    --sky-mid: #cfe4f2;
    --charcoal: #2a2c31;
    --navy: #1f3f8f;
    --white: #ffffff;
    --rating-red: #e8262a;
    --ink: #1b1b1b;
    --phone-blue: #2f7fd0;
  }
  * { margin: 0; padding: 0; box-sizing: border-box; }
  html, body { width: 1200px; height: 857px; overflow: hidden; background: #ffffff; }
  .card {
    position: relative; width: 1200px; height: 857px; overflow: hidden;
    background: linear-gradient(160deg, var(--white) 0%, var(--sky-light) 45%, var(--sky-mid) 100%);
    font-family: "Roboto", Arial, sans-serif;
  }
  .card__panel { position: absolute; inset: 0; }
  .brand-box {
    position: absolute; left: 42px; top: 0; width: 413px; height: 190px;
    background: var(--white); border-radius: 0 0 62px 62px;
    display: flex; align-items: center; justify-content: center; gap: 16px;
  }
  .brand-box__dot { width: 26px; height: 26px; border-radius: 50%; background: var(--navy); flex: none; }
  .brand-box__name { font-weight: 700; font-size: 30px; line-height: 1.1; color: var(--navy); }
  .headline {
    position: absolute; left: 55px; top: 212px;
    color: var(--white); font-weight: 900; font-size: 84px; line-height: 80px;
    letter-spacing: -1px; text-transform: uppercase;
  }
  .price-band { position: absolute; left: 0; top: 385px; width: 600px; height: 148px; }
  .price-band__list {
    position: absolute; left: 72px; top: 405px; list-style: none;
    color: var(--white); font-size: 40px; font-weight: 400; line-height: 60px;
  }
  .price-band__list strong { font-weight: 500; }
  .promise-list {
    position: absolute; left: 50px; top: 556px; list-style: none;
    color: var(--white); font-size: 24px; line-height: 35.5px;
  }
  .promise-list li { display: flex; align-items: center; gap: 10px; }
  .promise-list svg { flex: none; }
  .hero-photo {
    position: absolute; left: 570px; top: 130px; width: 600px; height: 585px;
    background: radial-gradient(ellipse at 55% 60%, #9a9c9f 0%, #c4c7ca 45%, rgba(220,232,242,0) 75%);
  }
  .rating {
    position: absolute; left: 860px; top: 510px; width: 340px; height: 200px;
    background: rgba(255,255,255,0.92); text-align: center; padding-top: 62px;
  }
  .rating__title { font-weight: 700; font-size: 56px; line-height: 56px; color: var(--rating-red); }
  .rating__text { font-family: "Tinos", "Times New Roman", serif; color: var(--ink); font-size: 23px; line-height: 23px; }
  .rating__source { font-family: "Tinos", "Times New Roman", serif; color: var(--ink); font-size: 11px; }
  .phone-bar {
    position: absolute; left: 546px; top: 711px; width: 654px; height: 116px;
    background: var(--charcoal); border-radius: 58px 0 0 58px;
    display: flex; align-items: center; padding-left: 44px; gap: 18px;
  }
  .phone-bar__number { color: var(--white); font-weight: 700; font-size: 76px; letter-spacing: 1px; }
</style>
</head>
<body>
<main class="card">
  <svg class="card__panel" width="1200" height="857" viewBox="0 0 1200 857" aria-hidden="true">
    <defs>
      <linearGradient id="panelBlue" x1="0" y1="0" x2="0" y2="1">
        <stop offset="0" stop-color="#0099dc"/>
        <stop offset="0.5" stop-color="#0a78c2"/>
        <stop offset="1" stop-color="#3d5aa6"/>
      </linearGradient>
    </defs>
    <polygon points="0,0 756,0 483,857 0,857" fill="url(#panelBlue)"/>
  </svg>

  <div class="brand-box">
    <span class="brand-box__dot"></span>
    <span class="brand-box__name">The Lantern<br>Point Guide</span>
  </div>

  <h1 class="headline">We Gurantee<br>Every Lead</h1>

  <svg class="price-band" viewBox="0 0 600 148" aria-hidden="true">
    <path d="M0 0 H570 Q600 0 592 28 L560 120 Q550 148 520 148 H0 Z" fill="#2a2c31"/>
  </svg>
  <ul class="price-band__list">
    <li><strong>$85</strong> Exclusive storm leads</li>
    <li><strong>$215</strong> commercial leads</li>
  </ul>

  <ul class="promise-list">
    <li><svg width="22" height="22" viewBox="0 0 22 22"><circle cx="11" cy="11" r="9.5" fill="none" stroke="#fff" stroke-width="1.6"/><path d="M9 6.5 L13.5 11 L9 15.5" fill="none" stroke="#fff" stroke-width="2"/></svg>They will have insurance</li>
    <li><svg width="22" height="22" viewBox="0 0 22 22"><circle cx="11" cy="11" r="9.5" fill="none" stroke="#fff" stroke-width="1.6"/><path d="M9 6.5 L13.5 11 L9 15.5" fill="none" stroke="#fff" stroke-width="2"/></svg>They will not have a dignal contract</li>
    <li><svg width="22" height="22" viewBox="0 0 22 22"><circle cx="11" cy="11" r="9.5" fill="none" stroke="#fff" stroke-width="1.6"/><path d="M9 6.5 L13.5 11 L9 15.5" fill="none" stroke="#fff" stroke-width="2"/></svg>Be in the area that you requested</li>
    <li><svg width="22" height="22" viewBox="0 0 22 22"><circle cx="11" cy="11" r="9.5" fill="none" stroke="#fff" stroke-width="1.6"/><path d="M9 6.5 L13.5 11 L9 15.5" fill="none" stroke="#fff" stroke-width="2"/></svg>They will not allow you to do inspecton</li>
    <li><svg width="22" height="22" viewBox="0 0 22 22"><circle cx="11" cy="11" r="9.5" fill="none" stroke="#fff" stroke-width="1.6"/><path d="M9 6.5 L13.5 11 L9 15.5" fill="none" stroke="#fff" stroke-width="2"/></svg>You will meet with the homeownwr</li>
    <li><svg width="22" height="22" viewBox="0 0 22 22"><circle cx="11" cy="11" r="9.5" fill="none" stroke="#fff" stroke-width="1.6"/><path d="M9 6.5 L13.5 11 L9 15.5" fill="none" stroke="#fff" stroke-width="2"/></svg>Sold Exclusively to you only</li>
    <li><svg width="22" height="22" viewBox="0 0 22 22"><circle cx="11" cy="11" r="9.5" fill="none" stroke="#fff" stroke-width="1.6"/><path d="M9 6.5 L13.5 11 L9 15.5" fill="none" stroke="#fff" stroke-width="2"/></svg>THEY have not been declined</li>
  </ul>

  <div class="hero-photo" role="img" aria-label="Photo of a small white house with a red roof sitting on stacks of banded hundred-dollar bills"></div>

  <div class="rating">
    <p class="rating__title">A+ Rating</p>
    <p class="rating__text">Highest Rating For</p>
    <p class="rating__text">Public Insurance Adjusters</p>
    <p class="rating__source">(Source: ClaimRank Review)</p>
  </div>

  <div class="phone-bar">
    <svg width="64" height="64" viewBox="0 0 24 24" aria-hidden="true">
      <path fill="#2f7fd0" d="M6.6 10.8a15.1 15.1 0 0 0 6.6 6.6l2.2-2.2a1 1 0 0 1 1-.25 11.4 11.4 0 0 0 3.6.57 1 1 0 0 1 1 1V20a1 1 0 0 1-1 1A17 17 0 0 1 3 4a1 1 0 0 1 1-1h3.5a1 1 0 0 1 1 1c0 1.25.2 2.45.57 3.57a1 1 0 0 1-.25 1z"/>
    </svg>
    <span class="phone-bar__number">888-555-0142</span>
  </div>
</main>
</body>
</html>
```